Local Directory Ad

We currently have an advertisement in our local directory (see attached). We would like to make it look more appealing.
Dimensions are 110mm H X 175mm W
We would like to keep the same colours and contact details remain the same.
Most of the content can remain the same, Just remove the line Tax effective remote area salary packaging and add in Self Managed Super Funds.We want to change mortgage broking to Mortgage Broking and Loan Structuring.

We want to change the line Local accountants Local Knowledge Local Experience - to something like local knowledge beyond compare or unsurpassed local knowledge but open to suggestions on this.

there are some good designs posted so far. I particulalry like the ones from pulmawick, korbu41, and the last one posted by wexlorunti and PLV. Keep up the good work guys

```html
<!DOCTYPE html>
<html lang="en">
<head>
<meta charset="utf-8">
<title>Brindell Accounting &amp; Finance – Directory Ad</title>
<link rel="stylesheet" href="https://fonts.googleapis.com/css2?family=Nunito:wght@800;900&family=Arimo:wght@400;700&family=Roboto+Condensed:wght@700&display=swap">
<style>
  :root {
    --red: #d0232a;
    --ink: #231f20;
    --charcoal: #242223;
    --white: #ffffff;
    --grey-band: #808285;
    --grey-text: #8c8c8c;
    --dark-copy: #2a2829;
  }
  * { box-sizing: border-box; margin: 0; padding: 0; }
  html, body { width: 1200px; height: 754px; overflow: hidden; background: var(--white); }
  .ad {
    position: relative; width: 1200px; height: 754px;
    background: var(--white); border: 2px solid var(--ink); overflow: hidden;
    font-family: "Arimo", Arial, sans-serif;
  }
  .column { position: absolute; top: 0; bottom: 0; }
  .column--left { left: 0; width: 343px; background: var(--red); }
  .column--middle { left: 343px; width: 514px; background: var(--white);
    box-shadow: inset 14px 0 12px -8px rgba(0,0,0,.35), inset -14px 0 12px -8px rgba(0,0,0,.35); }
  .column--right { left: 857px; right: 0; background: var(--charcoal); }

  .rule { position: absolute; height: 2px; }
  .rule--light { background: var(--white); }
  .rule--dark { background: var(--ink); }

  .title {
    position: absolute; top: 28px; font-family: "Nunito", Arial, sans-serif;
    font-weight: 900; font-size: 60px; line-height: 64px; letter-spacing: 1px;
  }
  .title--left { left: 34px; color: var(--white); }
  .title--middle { left: 37px; color: var(--red); }
  .title--right { left: 38px; color: var(--white); }

  .welcome {
    position: absolute; left: 28px; top: 197px;
    font-family: "Nunito", Arial, sans-serif; font-weight: 800;
    font-size: 40px; line-height: 65.5px; color: var(--dark-copy);
    text-shadow: 1px 1px 0 rgba(255,255,255,.25), 2px 2px 2px rgba(0,0,0,.35);
  }

  .services { position: absolute; left: 38px; top: 135px; list-style: none; }
  .services li {
    position: relative; padding-left: 30px; margin-bottom: 34px;
    font-weight: 700; font-size: 29px; line-height: 38px; color: var(--red);
  }
  .services li::before {
    content: ""; position: absolute; left: 0; top: 9px;
    width: 22px; height: 22px; border-radius: 50%; background: var(--ink);
  }

  .tagline {
    position: absolute; left: 0; right: 0; top: 196px; text-align: center;
    font-family: "Roboto Condensed", Arial, sans-serif; font-weight: 700;
    font-size: 46px; line-height: 84px; color: var(--grey-text);
  }

  .address {
    position: absolute; left: 11px; top: 628px; font-weight: 700;
    font-size: 19px; line-height: 26px; color: var(--white);
  }
  .web-band {
    position: absolute; left: 0; right: 0; top: 617px; height: 103px;
    background: var(--grey-band); text-align: center;
  }
  .web-band__url {
    display: block; margin-top: 22px; font-weight: 700;
    font-size: 37px; line-height: 40px; color: var(--white); letter-spacing: .5px;
  }
  .web-band__licence { display: block; font-size: 19px; line-height: 24px; color: var(--ink); }
  .contact {
    position: absolute; right: 14px; top: 628px; text-align: right;
    font-weight: 700; font-size: 19px; line-height: 26px; color: var(--white);
  }
</style>
</head>
<body>
<div class="ad">
  <section class="column column--left">
    <div class="rule rule--light" style="left:18px;right:14px;top:18px"></div>
    <h1 class="title title--left">Brindell</h1>
    <div class="rule rule--light" style="left:18px;right:14px;top:103px"></div>
    <p class="welcome">We are here<br>for you<br>all year round<br>to assist<br>with...</p>
    <div class="rule rule--light" style="left:18px;right:14px;top:614px"></div>
    <address class="address" style="font-style:normal">Shop 5 Quay Arcade<br>12 Marlow St Brindell<br>PO Box 88 Brindell 6790</address>
  </section>

  <section class="column column--middle">
    <div class="rule rule--dark" style="left:27px;right:30px;top:18px"></div>
    <h2 class="title title--middle">Accounting &amp;</h2>
    <div class="rule rule--dark" style="left:27px;right:30px;top:105px"></div>
    <ul class="services">
      <li>Accounting &amp; Taxation</li>
      <li>Business Advice</li>
      <li>GST and BAS’s</li>
      <li>Mortgage Broking and<br>Loan Structuring</li>
      <li>Bookkeeping</li>
      <li>Self Managed Super Funds</li>
    </ul>
    <div class="web-band">
      <span class="web-band__url">www.bafn.com.au</span>
      <span class="web-band__licence">Australian Credit Licence 400 118</span>
    </div>
  </section>

  <section class="column column--right">
    <div class="rule rule--light" style="left:14px;right:14px;top:18px"></div>
    <h2 class="title title--right">Finance</h2>
    <div class="rule rule--light" style="left:14px;right:14px;top:103px"></div>
    <p class="tagline">Our local<br>knowledge<br>is beyond<br>compare!</p>
    <div class="rule rule--light" style="left:14px;right:0;top:614px"></div>
    <p class="contact">E: reception@bafn.com.au<br>P: 9100 4812<br>F: 9100 4899</p>
  </section>
</div>
</body>
</html>
```